Business Card and Letterhead for Juniper Anvil - (Have Logo)

Update 4: Removed company reg no from business card details as it looked a bit out of place. Updated services list.
UPDATE 3
Sorry, I got the address a little bit wrong, have updated it below. Sorry for any inconvenience caused.
UPDATE 2
Finally I have the details for the business cards and letterhead. Submissions already made do not have to be updated unless shortlisted, if all new submissions could include the details for me, Marcus, that would be very much appreciated and help with the final shortlist selection. I intend to share a shortlist of the three best entries with past and existing customers for their feedback and opinions. Thank you all again for your time.
Here are the details.
Marcus Telby
Web Developer
T: 01632 960 418
E: marcus@juniperanvil.example
www.juniperanvil.example
Professional Photography
Web Solutions & E-Commerce
Audio & HD Video Production
Marketing & Promotions
Identity and Branding
Juniper Anvil Ltd
Suite 20938, 3rd Floor
212-224 Orchard Lane
London, N7 9QX
Company Reg. No: 05829147
The order and the layout of the information are of course down to the design, but the company registration number should be smaller and less prominent. The formatting of the telephone and email address using a T: and an E: I am not sure about and again if it is Tel: or Email: or Icons is up to the design.
The Company No. on the letterhead should read (somewhere in small text along the bottom):
Juniper Anvil is a Ltd Company registered in England & Wales, Registration No. 05829147.
The second business card details are
Oliver Brackley
Photographer
T: 01632 960 418
E: oliver@juniperanvil.example
Everything else the same of course.
Thank you again for all the submissions so far.
END OF UPDATE 2
-
UPDATE 1: Please do not alter the logo nor the logo colours. (This was a previous pixel forum project and I am extremely happy with it. The icon can stand alone of course, but I have had to eliminate all entries that have made it black and white, or reversed the icon.) I would like to thank everyone that has participated so far and am very grateful for all your thought and time.
End of Update 1
-
Original Brief:
I have attached the logo vector file.
Following a superb logo from a previous Pixel Forum project I am now looking for a business card design and (although less important) a letterhead as well.
I must admit I tried to do it myself but could only come up with the usual amateur stuff that in comparison to the quality of the logo looked awful.
About Us
Juniper Anvil Ltd will be a new company due to start in January. It is really just me (a web developer) and my friend (a photographer). We will be aiming at the usual small to medium sized businesses in the local area, selling various digital services including photographic services to the public, web hosting and development, commercial photography, modelling services (not us!), full video and film production and possibly a bit of marketing as well. (Really it is anything we can do professionally all lumped together! We met running seperate businesses which have both since closed)
We will not be competing on price. We plan to be expensive but fair. Certainly not the cheapest.
What we are looking for
Business Card
I imagine a double sided business card, which will be used for more than one person. I imagine the front to be the same for everyone and the persons details to be on the back, although this is of course only my thoughts and I am of course completely open to any ideas.
The card could also have a services list or a bit about what we do on it. It might feature the website address, our business address (mail forwarding address) or our registered company number.
Or it might have none of that, we are completely open to any ideas and have no real fixed opinions. I just want it to be really nice :-)
Letterhead (secondary importance)
We will make our decision primarily on the business card, although a mathcing letterhead would be fantastic. Something standardish in format and simple, although again, all ideas are welcomed.
I hope that is enough information but if you have any questions I will answer them as fully and as quickly as possible.
Thank you once again and I really look forward to seeing your ideas and picking a winner.
Marcus T.
Small businesses AND the general public
Film Production

```html
<!DOCTYPE html>
<html lang="en">
<head>
<meta charset="utf-8">
<title>Juniper Anvil – Business Card</title>
<link rel="stylesheet" href="https://fonts.googleapis.com/css2?family=Jost:wght@400;500;600;700&display=swap">
<style>
  :root {
    --canvas-bg: #ececec;
    --silver-light: #e4e5e7;
    --silver-mid: #c9cbce;
    --silver-dark: #b3b5b8;
    --ink: #1a1a1a;
    --ink-soft: #3a3a3a;
    --brand-red: #c0282d;
    --brand-grey: #8c8d8f;
    --card-black: #0d0d0d;
    --white: #ffffff;
  }
  * { box-sizing: border-box; margin: 0; padding: 0; }
  html, body {
    width: 1200px; height: 900px; overflow: hidden;
    background: var(--canvas-bg);
    font-family: "Jost", "Futura", sans-serif;
  }
  .stage { position: relative; width: 1200px; height: 900px; }

  .card {
    position: absolute;
    border-radius: 2px;
    box-shadow: 0 10px 28px rgba(0,0,0,.18), 0 2px 4px rgba(0,0,0,.12);
    overflow: hidden;
  }
  .brushed {
    background:
      linear-gradient(115deg, rgba(255,255,255,.35) 0%, rgba(255,255,255,0) 40%, rgba(255,255,255,.25) 70%, rgba(255,255,255,0) 100%),
      linear-gradient(180deg, var(--silver-light), var(--silver-mid) 55%, var(--silver-dark));
  }

  /* Front */
  .card-front {
    left: 70px; top: 295px; width: 540px; height: 310px;
    display: flex; flex-direction: column; justify-content: center; padding-left: 62px;
  }
  .wordmark { display: flex; align-items: center; gap: 14px; }
  .wordmark-square { width: 34px; height: 34px; background: var(--brand-red); flex: none; }
  .wordmark-name {
    font-weight: 600; font-size: 44px; letter-spacing: 1px; line-height: 1;
    text-transform: uppercase; color: var(--ink-soft);
  }
  .front-tagline {
    margin-top: 18px; font-size: 15px; font-weight: 400; letter-spacing: .6px;
    text-transform: uppercase; color: var(--ink);
  }

  /* Back */
  .card-back {
    left: 720px; top: 162px; width: 330px; height: 577px;
    display: flex; flex-direction: column;
  }
  .back-header {
    height: 118px; background: var(--card-black);
    display: flex; align-items: center; justify-content: center;
  }
  .back-header .wordmark-name { font-size: 30px; color: var(--brand-grey); }
  .back-header .wordmark-square { width: 24px; height: 24px; }
  .back-details {
    height: 158px; padding: 26px 22px 0 0; text-align: right;
  }
  .person-name {
    font-weight: 700; font-size: 27px; letter-spacing: 1px; color: var(--ink); text-transform: uppercase;
  }
  .person-role { font-size: 16px; color: var(--brand-red); margin-top: 2px; }
  .person-contact { margin-top: 12px; font-size: 13.5px; line-height: 1.35; color: var(--ink); text-transform: uppercase; letter-spacing: .3px; }

  .back-footer {
    position: relative; flex: 1; background: var(--card-black);
  }
  .footer-visual {
    position: absolute; inset: 12px 0 0 0;
    background: radial-gradient(ellipse at 65% 35%, #3f6f8f 0%, #2a3d52 35%, #141a22 70%, #0d0d0d 100%);
  }
  .company-address {
    position: absolute; left: 22px; bottom: 26px;
    color: var(--white); text-transform: uppercase; font-size: 13px; font-weight: 500; line-height: 1.35; letter-spacing: .4px;
  }
  .company-reg { font-size: 9px; font-weight: 400; margin-top: 2px; }
</style>
</head>
<body>
<main class="stage">

  <section class="card card-front brushed" aria-label="Business card front">
    <div class="wordmark">
      <span class="wordmark-square"></span>
      <span class="wordmark-name">Juniper Anvil</span>
    </div>
    <p class="front-tagline">Web Solutions + Photography + Video Production</p>
  </section>

  <section class="card card-back" aria-label="Business card back">
    <header class="back-header">
      <div class="wordmark">
        <span class="wordmark-square"></span>
        <span class="wordmark-name">Juniper Anvil</span>
      </div>
    </header>
    <div class="back-details brushed">
      <h1 class="person-name">Marcus Telby</h1>
      <p class="person-role">Web Developer</p>
      <p class="person-contact">T: 01632 960 418<br>E: marcus@juniperanvil.example</p>
    </div>
    <footer class="back-footer">
      <div class="footer-visual" role="img" aria-label="Wall of photo and video thumbnails receding into darkness"></div>
      <address class="company-address" style="font-style:normal">
        Juniper Anvil Ltd.<br>
        212-224 Orchard Lane<br>
        London, N7 9QX
        <div class="company-reg">Company Reg. No: 05829147</div>
      </address>
    </footer>
  </section>

</main>
</body>
</html>
```